Postcard 4.25"x 6" template

We need a postcard template to send information about our wellness clinic's classes and groups.
The mailing side needs space for changeable text to talk about the clinic and brief info about our classes and groups, in addition to meeting the Halvern Courier Network requirements for address and return address area. The return address space can be fixed with our clinic's name and address on it.
The other side should be a dynamic calendar. For the time being, please use the information listed for the month of February. However, this should be changeable so that we can update the month and the events.
Somewhere on the postcard should also be a link to our website's events page:
http://www.brovelaclinic.example/events
Please work with our website for guidance on the look and feel of our marketing materials.
Overall it should have a natural feel.
It needs to be able to be printed at a regular printing shop and look good. It should not require a large commercial printer.
It will also need to be editable in a Word Document format.

```html
<!DOCTYPE html>
<html lang="en">
<head>
<meta charset="utf-8">
<title>Brovela Clinic – Groups and Classes Postcard</title>
<link rel="stylesheet" href="https://fonts.googleapis.com/css2?family=Open+Sans:ital,wght@0,400;0,600;1,400&display=swap">
<style>
  :root {
    --page: #ffffff;
    --leaf-green: #5dba4c;
    --leaf-green-light: #6cc35b;
    --ink-light: #ffffff;
    --cal-bg: #f5f6ef;
    --cal-line: #dde2d3;
    --cal-num: #8a8a84;
    --cal-muted: #cfd1c8;
    --cal-title: #9aa46a;
    --chip: #8ca862;
    --chip-edge: #6f8b4a;
    --brand-green: #4fa83f;
    --brand-grey: #7c7f78;
  }
  * { box-sizing: border-box; margin: 0; padding: 0; }
  html, body { width: 1200px; height: 800px; overflow: hidden; background: var(--page); }
  body { font-family: "Open Sans", Arial, sans-serif; position: relative; }

  .postcard {
    position: absolute; left: 76px; top: 38px; width: 1046px; height: 727px;
    background: radial-gradient(circle at 30% 40%, var(--leaf-green-light), var(--leaf-green) 70%);
    color: var(--ink-light);
    overflow: hidden;
  }
  .tagline {
    position: absolute; left: 0; right: 0; top: 18px;
    text-align: center; font-style: italic; font-size: 19px; letter-spacing: 0.2px;
  }
  .section-title {
    position: absolute; left: 39px; top: 75px; font-size: 13px; letter-spacing: 0.2px;
  }
  .class-list {
    position: absolute; left: 39px; top: 111px; width: 460px; list-style: none;
    font-size: 13.6px; line-height: 19px;
  }
  .class-list li { position: relative; margin-bottom: 19px; }
  .class-list li::before {
    content: ""; position: absolute; left: -19px; top: 6px;
    width: 7px; height: 7px; border-radius: 50%; background: var(--ink-light);
  }

  .calendar-frame {
    position: absolute; left: 529px; top: 80px; width: 483px; height: 479px;
    background: var(--page); border-radius: 42px; overflow: hidden;
  }
  .calendar {
    position: absolute; left: 5px; top: 37px; width: 462px; height: 440px;
    background: var(--cal-bg);
  }
  .calendar-pebbles {
    position: absolute; left: 0; top: 32px; width: 48px; height: 78px;
    background: radial-gradient(ellipse at 20% 55%, #ffffff 0%, #e9ebe6 45%, rgba(245,246,239,0) 75%);
  }
  .cal-head { position: absolute; left: 0; right: 0; top: 5px; height: 22px; }
  .cal-nav {
    position: absolute; top: 0; height: 18px; width: 27px;
    border: 1px solid #c9c9c2; background: #f1f1ec; border-radius: 3px;
  }
  .cal-nav svg { display: block; margin: 4px auto 0; }
  .cal-today {
    position: absolute; left: 59px; top: 0; height: 18px; padding: 0 6px;
    border: 1px solid #c9c9c2; background: #f1f1ec; border-radius: 3px;
    font-size: 9px; line-height: 16px; color: #555;
  }
  .cal-title {
    position: absolute; left: 170px; width: 160px; top: 1px; text-align: center;
    font-size: 12.5px; color: var(--cal-title);
  }
  .cal-grid {
    position: absolute; left: 0; top: 30px; width: 462px;
    border-collapse: collapse; table-layout: fixed;
  }
  .cal-grid th {
    height: 14px; font-size: 8px; font-weight: 600; color: #8b8b85;
    border: 1px solid var(--cal-line);
  }
  .cal-grid td {
    border: 1px solid var(--cal-line); vertical-align: top; text-align: right;
    font-size: 8.5px; color: var(--cal-num); padding: 1px 3px 0 2px;
  }
  .cal-grid .other { color: var(--cal-muted); }
  .cal-grid tr.week td { height: 55px; }
  .cal-grid tr.week-busy td { height: 119px; }
  .event {
    text-align: left; margin: 3px 0 0 0; padding: 1px 2px;
    background: var(--chip); border: 1px solid var(--chip-edge); border-radius: 2px;
    color: var(--ink-light); font-size: 6.6px; line-height: 8.8px;
  }
  .event + .event { margin-top: 2px; }
  .event p + p { margin-top: 1px; }

  .events-link {
    position: absolute; left: 579px; top: 582px; font-size: 13.6px; line-height: 19px;
  }

  .brand-tab {
    position: absolute; left: 390px; top: 642px; width: 279px; height: 90px;
    background: var(--page); border-radius: 40px 40px 0 0;
    display: flex; align-items: center; justify-content: center; gap: 8px;
  }
  .brand-dot { width: 14px; height: 14px; border-radius: 50%; background: var(--brand-green); }
  .brand-name { font-size: 15px; letter-spacing: 1.5px; color: var(--brand-grey); }
</style>
</head>
<body>
<main class="postcard">
  <h1 class="tagline">HOLISTIC, NATUROPATHIC, INTEGRATIVE MENTAL HEALTH CARE: WE’RE HEALING MINDS</h1>

  <h2 class="section-title">GROUPS AND CLASSES</h2>
  <ul class="class-list">
    <li>Group Accupuncture<br>10am - noon, every Monday starting 2/4, with Marla Quinn<br>5pm - 7pm, every Wednesday starting 1/8, with Tessa Holloway</li>
    <li>Group Therapy<br>6:30pm - 8pm, every Tuesday starting 2/4, with Lacey Dorran</li>
    <li>Healing from Trauma and Addiction Group<br>7:30pm - 9pm, every Wednesday starting 2/5, with Lacey Dorran</li>
    <li>Yoga After Trauma: Reclaiming Body and Mind<br>9:30am - 11am, every Wednesday starting 2/5, with Renata</li>
    <li>IV Therapy<br>9am - 1pm, every Monday and Thursday starting 2/3, with Dr. Simone<br>Varga, ND</li>
    <li>Food Story Transformation Program<br>10am - noon, every Saturday starting 2/8, with Owen Pratt</li>
    <li>Physiology for Herbalists<br>6:30pm - 9:30pm, every Thursday starting 2/20 until 3/27, with Helena<br>Marchetti</li>
    <li>The Power of Becoming Who You Are: Holistic Healing with Mindfulness<br>6:30pm - 8:30pm, every Wednesday starting 4/2 until 5/7, with Renata</li>
  </ul>

  <section class="calendar-frame" aria-label="February 2014 calendar">
    <div class="calendar">
      <div class="cal-head">
        <span class="cal-nav" style="left:2px"><svg width="8" height="8" viewBox="0 0 8 8"><path d="M6 0 L1 4 L6 8 Z" fill="#333"/></svg></span>
        <span class="cal-nav" style="left:29px"><svg width="8" height="8" viewBox="0 0 8 8"><path d="M2 0 L7 4 L2 8 Z" fill="#333"/></svg></span>
        <span class="cal-today">today</span>
        <span class="cal-title">FEBRUARY 2014</span>
      </div>
      <table class="cal-grid">
        <thead>
          <tr><th>Sun</th><th>Mon</th><th>Tue</th><th>Wed</th><th>Thu</th><th>Fri</th><th>Sat</th></tr>
        </thead>
        <tbody>
          <tr class="week"><td class="other">26</td><td class="other">27</td><td class="other">28</td><td class="other">29</td><td class="other">30</td><td class="other">31</td><td>1</td></tr>
          <tr class="week-busy">
            <td>2</td>
            <td>3
              <div class="event"><p>Group IV Session</p><p>Group Acupuncture</p></div>
              <div class="event"><p>Group Acupuncture with Marla Quinn</p></div>
            </td>
            <td>4</td>
            <td>5
              <div class="event"><p>Yoga After Trauma: Reclaiming the Body and Mind</p><p>“Happy Hour” Group Acupuncture</p></div>
              <div class="event"><p>Healing From Trauma and Addiction</p></div>
            </td>
            <td>6</td><td>7</td><td>8</td>
          </tr>
          <tr class="week"><td>9</td><td>10</td><td>11</td><td>12</td><td>13</td><td>14</td><td>15</td></tr>
          <tr class="week"><td>16</td><td>17</td><td>18</td><td>19</td><td>20</td><td>21</td><td>22</td></tr>
          <tr class="week"><td>23</td><td>24</td><td>25</td><td>26</td><td>27</td><td>28</td><td class="other">1</td></tr>
          <tr class="week"><td class="other">2</td><td class="other">3</td><td class="other">4</td><td class="other">5</td><td class="other">6</td><td class="other">7</td><td class="other">8</td></tr>
        </tbody>
      </table>
      <div class="calendar-pebbles" role="img" aria-label="Soft photo of smooth white pebbles"></div>
    </div>
  </section>

  <p class="events-link">To know more about the upcoming events visit our website:<br>http://www.brovelaclinic.example/events</p>

  <div class="brand-tab">
    <span class="brand-dot"></span>
    <span class="brand-name">BROVELA CLINIC</span>
  </div>
</main>
</body>
</html>
```